Shopguidance.net

I've attached two different logo's which I both like and would like to see different designs with each logo. I'm starting a retail consulting business and blog. You can view the start of my project at shopguidance.net to get an idea of what I'm creating.
Looking for a design that says creative, strategic and community.
Updates
Hello Everyone,
Thank you for the amazing design so far.
What I Like
- double sided designs, front and back
- one side should be white or green. Customers cannot write on or make notes on an all black card
- Simple, cool, creative is best
My business card will only have the following
- Instagram
- Facebook
- Email
- Website
My new Tag line is
Think Smart. Lead Smart. Work Smart.
My title will be:
Tobin Marlowe
Retail Consultant
Please submit 1 or 2 designs with these specifications.
Thank you,
Tobin
Reason: Looking for a few more designs and have now committed the project and it is no longer refundable. Please read brief and follow specific instructions.
Looking for something simple yet creative. Something that may stand out from most cards.
Thank you,
Tobin
Thank you,
Tobin
Target Market(s)
My main target is retail managers and retail businesses that are focused on leadership and people development.
Industry/Entity Type
Retail
Look and feel
Each slider illustrates characteristics of the customer's brand and the style your logo design should communicate.

```html
<!DOCTYPE html>
<html lang="en">
<head>
<meta charset="utf-8">
<title>Shopguidance – Business Card</title>
<link rel="stylesheet" href="https://fonts.googleapis.com/css2?family=Jost:wght@400;500;600&family=Open+Sans:wght@400;700&family=Pinyon+Script&display=swap">
<style>
  :root {
    --backdrop: #2f2f30;
    --green-deep: #06a448;
    --green-light: #62c464;
    --green-line: #2fb34a;
    --band-black: #1c1c1c;
    --paper: #ffffff;
    --ink: #262626;
    --ink-soft: #444444;
    --white: #ffffff;
  }
  * { box-sizing: border-box; margin: 0; padding: 0; }
  html, body { width: 1200px; height: 819px; overflow: hidden; }
  body {
    background: var(--backdrop);
    font-family: "Open Sans", Arial, sans-serif;
    position: relative;
  }
  .card {
    position: absolute;
    top: 255px;
    width: 540px;
    height: 309px;
    border-radius: 4px;
    overflow: hidden;
    box-shadow: 0 14px 30px rgba(0,0,0,0.45);
  }
  .card--front {
    left: 40px;
    background: linear-gradient(150deg, var(--green-deep) 0%, var(--green-light) 100%);
    display: flex;
    align-items: center;
    justify-content: center;
  }
  .card--back {
    left: 620px;
    background: var(--paper);
  }
  .brand {
    display: flex;
    align-items: center;
    gap: 12px;
    font-family: "Jost", sans-serif;
    font-weight: 500;
    color: var(--white);
  }
  .brand__dot {
    border-radius: 50%;
    flex: none;
  }
  .card--front .brand { font-size: 44px; }
  .card--front .brand__dot { width: 42px; height: 42px; background: var(--white); }

  .back__band {
    height: 112px;
    background: var(--band-black);
    border-bottom: 6px solid var(--green-line);
    display: flex;
    align-items: center;
    justify-content: center;
  }
  .back__band .brand { font-size: 34px; }
  .back__band .brand__dot { width: 34px; height: 34px; background: var(--green-line); }

  .back__body {
    position: relative;
    height: 191px;
  }
  .person {
    position: absolute;
    left: 32px;
    top: 30px;
  }
  .person__name {
    font-size: 22px;
    font-weight: 700;
    color: var(--ink);
    line-height: 1.1;
  }
  .person__title {
    font-size: 12px;
    letter-spacing: 0.5px;
    color: var(--ink-soft);
    margin-top: 2px;
  }
  .divider {
    position: absolute;
    left: 262px;
    top: 18px;
    width: 1px;
    height: 84px;
    background: var(--ink);
  }
  .contacts {
    position: absolute;
    left: 278px;
    top: 20px;
    list-style: none;
    font-size: 12.5px;
    color: var(--ink);
    line-height: 20px;
    white-space: nowrap;
  }
  .contacts li { display: flex; align-items: center; gap: 7px; }
  .contacts__mark {
    width: 11px; height: 11px; border-radius: 50%;
    background: var(--ink); flex: none;
  }
  .tagline {
    position: absolute;
    left: 0; right: 0;
    top: 122px;
    text-align: center;
    white-space: nowrap;
    font-family: "Pinyon Script", cursive;
    font-size: 27px;
    line-height: 40px;
    letter-spacing: 1px;
    word-spacing: 8px;
    color: var(--ink-soft);
  }
</style>
</head>
<body>
  <section class="card card--front" aria-label="Card front">
    <div class="brand"><span class="brand__dot"></span><span>Shopguidance</span></div>
  </section>

  <section class="card card--back" aria-label="Card back">
    <header class="back__band">
      <div class="brand"><span class="brand__dot"></span><span>Shopguidance</span></div>
    </header>
    <div class="back__body">
      <div class="person">
        <p class="person__name">Tobin Marlowe</p>
        <p class="person__title">RETAIL CONSULTANT</p>
      </div>
      <span class="divider"></span>
      <ul class="contacts">
        <li><span class="contacts__mark"></span>snapfeed.com/shopguidance</li>
        <li><span class="contacts__mark"></span>friendwall.com/shopguidance</li>
        <li><span class="contacts__mark"></span>hello@shopguidance.net</li>
        <li><span class="contacts__mark"></span>www.shopguidance.net</li>
      </ul>
      <p class="tagline">Think Smart. Lead Smart. Work Smart.</p>
    </div>
  </section>
</body>
</html>
```